Wrenhollow Acres Organic Flower Farm, Farmer Florist

I am a flower grower and florist, so I do everything from the field to the vase. I want to include my website, phone, email and instagram

```html
<!DOCTYPE html>
<html lang="en">
<head>
<meta charset="utf-8">
<title>Wrenhollow Acres – Business Cards</title>
<link href="https://fonts.googleapis.com/css2?family=Cinzel:wght@500&family=Comfortaa:wght@600&family=Didact+Gothic&family=Gelasio:wght@500&display=swap" rel="stylesheet">
<style>
  :root {
    --backdrop: #dcdcdc;
    --card: #ffffff;
    --maroon: #5c2b30;
    --sage: #9bd0a6;
    --blush: #f08d8d;
    --ink: #2b2326;
    --divider: #d9c9cc;
    --bloom-gold: #e6b94a;
    --bloom-rust: #c9762f;
    --bloom-leaf: #a7a84f;
  }
  * { box-sizing: border-box; margin: 0; padding: 0; }
  html, body {
    width: 1200px; height: 1067px; overflow: hidden;
    background: var(--backdrop);
  }
  .canvas { position: relative; width: 1200px; height: 1067px; }

  .card {
    position: absolute; left: 280px;
    width: 640px; height: 366px;
    background: var(--card);
    border-radius: 22px;
    overflow: hidden;
    box-shadow: 0 6px 18px rgba(0,0,0,0.12);
  }
  .card--front { top: 150px; }
  .card--back  { top: 560px; }

  .wordmark {
    position: absolute;
    font-family: "Cinzel", serif;
    font-weight: 500;
    color: var(--maroon);
    letter-spacing: 4px;
    text-align: center;
    display: flex; align-items: center; gap: 12px;
  }
  .wordmark__dot {
    flex: none;
    width: 12px; height: 12px; border-radius: 50%;
    background: var(--sage);
  }

  /* front */
  .card--front .wordmark {
    left: 0; right: 0; top: 78px; justify-content: center;
    font-size: 44px;
  }
  .est {
    position: absolute; left: 0; right: 0; top: 140px;
    text-align: center;
    font-family: "Cinzel", serif; font-size: 13px; letter-spacing: 5px;
    color: var(--maroon);
  }
  .blooms {
    position: absolute; left: 70px; right: 40px; top: 190px; height: 112px;
    border-radius: 60px 60px 0 0;
    background: linear-gradient(90deg, var(--bloom-rust) 0%, var(--bloom-gold) 35%, var(--bloom-gold) 60%, var(--bloom-leaf) 100%);
    opacity: 0.85;
  }
  .band {
    position: absolute; bottom: 0; height: 64px;
    display: flex; align-items: center; justify-content: center;
    font-family: "Comfortaa", sans-serif; font-weight: 600;
    color: #fff;
    white-space: nowrap;
  }
  .card--front .band {
    left: 0; right: 0; background: var(--maroon);
    font-size: 17px; letter-spacing: 3px; text-transform: uppercase;
  }

  /* back */
  .card--back .wordmark {
    left: 0; width: 330px; top: 120px; justify-content: center;
    font-size: 32px; letter-spacing: 3px;
  }
  .card--back .est { left: 0; right: auto; width: 330px; top: 168px; font-size: 11px; }
  .card--back .band--role {
    left: 0; width: 330px; background: var(--maroon);
    font-size: 15px;
  }
  .band--social {
    position: absolute; bottom: 0; left: 330px; right: 0; height: 78px;
    background: var(--sage);
    display: flex; align-items: center; gap: 8px; padding: 0 16px 0 18px;
    font-family: "Didact Gothic", sans-serif; font-size: 12px; color: #fff;
    white-space: nowrap;
  }
  .social-dot {
    flex: none;
    width: 12px; height: 12px; border: 1.5px solid #fff; border-radius: 50%;
  }
  .divider {
    position: absolute; left: 330px; top: 40px; height: 248px;
    border-left: 1px solid var(--divider);
  }
  .person {
    position: absolute; left: 368px; top: 44px;
  }
  .person__name {
    font-family: "Gelasio", serif; font-weight: 500;
    font-size: 38px; color: var(--ink); letter-spacing: 1px;
  }
  .person__role {
    margin-top: 2px;
    font-family: "Didact Gothic", sans-serif; font-size: 16px;
    color: var(--blush); letter-spacing: 1px;
  }
  .sprig {
    position: absolute; left: 470px; top: 100px; width: 130px; height: 10px;
    border-radius: 5px;
    background: linear-gradient(90deg, #b9c7a6, var(--blush));
    opacity: 0.8;
  }
  .contact {
    position: absolute; left: 368px; top: 150px;
    list-style: none;
    font-family: "Didact Gothic", sans-serif; font-size: 15px; color: var(--ink);
  }
  .contact li { display: flex; align-items: center; gap: 10px; margin-bottom: 9px; }
  .contact svg { width: 14px; height: 14px; flex: none; }
</style>
</head>
<body>
<main class="canvas">

  <section class="card card--front" aria-label="Business card front">
    <div class="wordmark"><span class="wordmark__dot"></span>Wrenhollow</div>
    <p class="est">Est. 2019</p>
    <div class="blooms" role="img" aria-label="Illustrated sunflowers, autumn leaves and berry sprigs"></div>
    <div class="band">Growing flowers &amp; growing a community</div>
  </section>

  <section class="card card--back" aria-label="Business card back">
    <div class="wordmark"><span class="wordmark__dot"></span>Wrenhollow</div>
    <p class="est">Est. 2019</p>
    <div class="band band--role">Organic Flower Farmer &amp; Designer</div>

    <div class="divider"></div>

    <div class="person">
      <h1 class="person__name">Maren Holt</h1>
      <p class="person__role">Florist</p>
    </div>
    <div class="sprig" role="img" aria-label="Small watercolour flower sprig"></div>

    <ul class="contact">
      <li>
        <svg viewBox="0 0 16 16" aria-hidden="true"><path fill="#2b2326" d="M3.6 1.5l2.3 2.4-1.2 1.8a9 9 0 0 0 5.6 5.6l1.8-1.2 2.4 2.3-1.4 2.1C7.8 14.9 1.1 8.2 1.5 2.9z"/></svg>
        +1 303-555-0148
      </li>
      <li>
        <svg viewBox="0 0 16 16" aria-hidden="true"><rect x="1.5" y="3.5" width="13" height="9" fill="none" stroke="#2b2326" stroke-width="1.5"/><path d="M1.5 3.5L8 9l6.5-5.5" fill="none" stroke="#2b2326" stroke-width="1.5"/></svg>
        maren@wrenhollowacres.com
      </li>
      <li>
        <svg viewBox="0 0 16 16" aria-hidden="true"><circle cx="8" cy="8" r="6.5" fill="#2b2326"/><path d="M1.5 8h13M8 1.5c3 3.5 3 9.5 0 13M8 1.5c-3 3.5-3 9.5 0 13" fill="none" stroke="#fff" stroke-width="1"/></svg>
        www.wrenhollowacres.com
      </li>
    </ul>

    <div class="band--social">
      <span class="social-dot"></span>
      <span class="social-url">https://www.petalgram.com/wrenhollowacres</span>
    </div>
  </section>

</main>
</body>
</html>
```